job vacancy cover page

I need to design a one pager for a job I'd like to apply for. The one I have done looks shit and amateur!! Wanting it to look amazing and professional (Not too professional though as they are pretty young and fun).

```html
<!DOCTYPE html>
<html lang="en">
<head>
<meta charset="utf-8">
<title>Why Me? Why Brightfield? Cover Page</title>
<link href="https://fonts.googleapis.com/css2?family=Nunito:wght@800&family=Poppins:wght@400;600&display=swap" rel="stylesheet">
<style>
:root{
  --blue-a:#1f6ff2;--blue-b:#14c9e0;
  --purple-a:#c24ee6;--purple-b:#8d7df8;
  --teal-a:#21be97;--teal-b:#17c7df;
  --gold:#f2b766;--gold-b:#f5c57f;
  --pink:#e55681;--pink-b:#e3668b;
  --orange-a:#f48a2a;--orange-b:#fb8f5a;
  --ink:#3c3f4a;--slide:#f8f9fb;
}
*{margin:0;padding:0;box-sizing:border-box}
html,body{width:1062px;height:1200px;overflow:hidden;background:#fff}
body{position:relative;font-family:"Poppins",sans-serif;color:var(--ink)}
.slide{position:absolute;left:143px;width:742px;height:412px;background:var(--slide);box-shadow:0 18px 40px rgba(40,50,80,.14)}
.slide--cards{top:124px}
.slide--blobs{top:636px}
.dots{position:absolute;display:flex;gap:3px}
.dots i{width:5px;height:5px;border-radius:50%;display:block}
.dots--cool i:nth-child(1){background:#1f6ff2}.dots--cool i:nth-child(2){background:#17c7df}.dots--cool i:nth-child(3){background:#8d7df8}
.dots--warm i:nth-child(1){background:#f2b766}.dots--warm i:nth-child(2){background:#e55681}.dots--warm i:nth-child(3){background:#f48a2a}
.section-tab{position:absolute;left:258px;width:227px;height:47px}
.section-tab svg{position:absolute;inset:0}
.section-tab__rule{position:absolute;left:98px;top:10px;width:32px;height:2px;border-radius:2px}
.section-tab__title{position:absolute;left:0;right:0;top:16px;text-align:center;font-family:"Nunito",sans-serif;font-weight:800;font-size:15px}
.title-me{color:#1790e8}
.title-company{background:linear-gradient(90deg,#e8396b,#f47a3a);-webkit-background-clip:text;background-clip:text;color:transparent}
.card{position:absolute;width:214px;height:118px;border:1.5px solid;border-radius:6px;background:#fbfcfd;overflow:hidden}
.card--blue{border-color:#2a8df0}.card--purple{border-color:#a86cef}.card--teal{border-color:#1fc2c4}
.card--gold{border-color:#f2bb72}.card--pink{border-color:#e45b86}.card--orange{border-color:#f58d3f}
.pill{position:absolute;height:30px;border-radius:15px;color:#fff;font-size:9.6px;display:flex;align-items:center;justify-content:center;gap:12px;box-shadow:0 4px 10px rgba(0,0,0,.12);z-index:2;white-space:nowrap}
.pill svg{width:14px;height:14px}
.pill--blue{background:linear-gradient(90deg,var(--blue-a),var(--blue-b))}
.pill--purple{background:linear-gradient(90deg,var(--purple-a),var(--purple-b))}
.pill--teal{background:linear-gradient(90deg,var(--teal-a),var(--teal-b))}
.pill--gold{background:var(--gold)}
.pill--pink{background:var(--pink)}
.pill--orange{background:linear-gradient(90deg,var(--orange-a),var(--orange-b))}
.points{position:absolute;font-size:8.5px;line-height:15.1px;list-style:none;z-index:1}
.points li{position:relative;padding-left:9px}
.points li::before{content:"";position:absolute;left:0;top:6.5px;width:3px;height:3px;border-radius:50%;background:currentColor}
.points strong{font-weight:600;display:block}
.card .points{left:13px;top:18px;right:11px;color:#4a4d57}
.card .points--lead{left:26px}
.ghost{position:absolute;opacity:.07}
.sidebar{position:absolute;left:0;top:0;width:46px;height:412px}
.side-label{position:absolute;transform:rotate(-90deg);transform-origin:left top;font-family:"Nunito",sans-serif;font-weight:800;font-size:15px;white-space:nowrap}
.side-label__rule{position:absolute;width:2px;border-radius:2px}
.divider{position:absolute;left:46px;right:0;top:206px;height:4px;background:#f2f3f6}
.blob{position:absolute;filter:drop-shadow(0 6px 6px rgba(30,40,70,.14))}
.blob svg{width:100%;height:100%;display:block}
.blob-text{color:#fff}
.placeholder{position:absolute;border-radius:8px}
</style>
</head>
<body>

<section class="slide slide--cards">
  <div class="dots dots--cool" style="left:16px;top:15px"><i></i><i></i><i></i></div>
  <div class="dots dots--warm" style="left:707px;top:15px"><i></i><i></i><i></i></div>

  <div class="section-tab" style="top:0">
    <svg viewBox="0 0 227 47" preserveAspectRatio="none"><path d="M0 0H227Q214 4 203 30Q196 47 170 47H57Q31 47 24 30Q13 4 0 0Z" fill="#fff"/></svg>
    <span class="section-tab__rule" style="background:#2ec5e6"></span>
    <h2 class="section-tab__title title-me">Why Me?</h2>
  </div>

  <div class="pill pill--blue" style="left:78px;top:52px;width:136px">
    <span role="img" aria-label="Flying superhero icon" style="width:12px;height:12px;border-radius:50%;background:rgba(255,255,255,.85);display:block"></span>If I was a superhero
  </div>
  <div class="card card--blue" style="left:39px;top:67px">
    <div class="placeholder ghost" role="img" aria-label="Faint flying superhero illustration" style="left:130px;top:44px;width:70px;height:60px;background:#5a6273"></div>
    <ul class="points points--lead">
      <li style="padding-left:0"><strong>My four superpowers would be:</strong></li>
      <li>Proactiveness</li><li>Creativity</li><li>Pride in my work</li><li>Organisational skills</li>
    </ul>
  </div>

  <div class="pill pill--purple" style="left:301px;top:52px;width:141px">
    <svg viewBox="0 0 16 16" fill="none" stroke="#fff" stroke-width="1.3"><rect x="1" y="2" width="11" height="8"/><path d="M3 7l2-2 2 2 2-3"/><circle cx="12.5" cy="9" r="1.6" fill="#fff"/><path d="M10 15v-2a2.5 2.5 0 015 0v2" fill="#fff"/></svg>Some of my success
  </div>
  <div class="card card--purple" style="left:265px;top:67px">
    <ul class="points">
      <li>Increased client workshops by 85% across accounts.</li>
      <li>Delivered double digit revenue increase.</li>
      <li>Re-designed workshops for virtual delivery, maintaining key relationships.</li>
    </ul>
  </div>

  <div class="pill pill--teal" style="left:527px;top:52px;width:141px;justify-content:flex-start;padding-left:18px;gap:30px">
    <svg viewBox="0 0 16 16" fill="#fff"><rect x="2" y="2" width="5.5" height="5.5" rx="1"/><rect x="8.5" y="2" width="5.5" height="5.5" rx="1"/><rect x="2" y="8.5" width="5.5" height="5.5" rx="1"/><rect x="8.5" y="8.5" width="5.5" height="5.5" rx="1"/></svg>Passion
  </div>
  <div class="card card--teal" style="left:491px;top:67px">
    <ul class="points">
      <li>The development of others and / or their teams.</li>
      <li>Helping people learn and be successful in life and in their careers.</li>
      <li>Exceptional client</li><li>experiences</li>
    </ul>
  </div>

  <div class="section-tab" style="top:208px">
    <svg viewBox="0 0 227 47" preserveAspectRatio="none"><path d="M0 0H227Q214 4 203 30Q196 47 170 47H57Q31 47 24 30Q13 4 0 0Z" fill="#fff"/></svg>
    <span class="section-tab__rule" style="background:#f58a63"></span>
    <h2 class="section-tab__title title-company">Why Brightfield?</h2>
  </div>

  <div class="pill pill--gold" style="left:75px;top:261px;width:141px">
    <svg viewBox="0 0 16 16" fill="none" stroke="#fff" stroke-width="1.3"><circle cx="8" cy="8" r="6.5"/><path d="M8 1.5V8l5 4M8 8l-5 3.5"/></svg>Values that stood out
  </div>
  <div class="card card--gold" style="left:39px;top:276px">
    <svg class="ghost" style="left:126px;top:36px;width:72px;height:72px" viewBox="0 0 32 32" fill="none" stroke="#3c3f4a" stroke-width="2"><circle cx="16" cy="16" r="14"/><path d="M16 2v14l10 8M16 16L5 24"/></svg>
    <ul class="points">
      <li>Proactiveness</li><li>Creativity</li><li>Pride in my work</li><li>Organisational skills</li>
    </ul>
  </div>

  <div class="pill pill--pink" style="left:301px;top:261px;width:141px">
    <svg viewBox="0 0 16 16" fill="#fff"><rect x="1" y="9" width="2.5" height="6"/><rect x="4.8" y="7" width="2.5" height="8"/><rect x="8.6" y="8" width="2.5" height="7"/><rect x="12.4" y="10" width="2.5" height="5"/><circle cx="6" cy="3" r="2"/></svg>What you offer
  </div>
  <div class="card card--pink" style="left:265px;top:276px">
    <ul class="points">
      <li>Learning &amp; Developing</li><li>Team</li><li>Flexibility</li><li>Fun</li>
    </ul>
  </div>

  <div class="pill pill--orange" style="left:527px;top:261px;width:141px">
    <svg viewBox="0 0 16 16" fill="none" stroke="#fff" stroke-width="1.3"><rect x="1" y="2" width="14" height="9.5"/><path d="M3.5 9l3-3 2 2 4-4M8 11.5V14M5 15l3-1.5 3 1.5"/></svg>Interesting projects
  </div>
  <div class="card card--orange" style="left:491px;top:276px">
    <svg class="ghost" style="left:130px;top:40px;width:64px;height:58px" viewBox="0 0 16 16" fill="none" stroke="#3c3f4a" stroke-width="1.2"><rect x="1" y="1" width="14" height="10.5"/><path d="M3.5 9l3-3 2 2 4-4M8 11.5V15"/></svg>
    <ul class="points">
      <li>Ovela - Leadership development and team effectiveness</li>
      <li>Hartwell – Change management for true transformation</li>
      <li>Lyra – Customer centricity at Australia's most iconic department store</li>
    </ul>
  </div>
</section>

<section class="slide slide--blobs">
  <svg width="0" height="0" style="position:absolute">
    <defs>
      <linearGradient id="g-blue" x1="0" y1="0" x2="1" y2="0.4"><stop offset="0" stop-color="#1f6ff2"/><stop offset="1" stop-color="#14c9e0"/></linearGradient>
      <linearGradient id="g-purple" x1="0" y1="0" x2="1" y2="0.4"><stop offset="0" stop-color="#c24ee6"/><stop offset="1" stop-color="#8d7df8"/></linearGradient>
      <linearGradient id="g-teal" x1="0" y1="0" x2="1" y2="0.4"><stop offset="0" stop-color="#21be97"/><stop offset="1" stop-color="#17c7df"/></linearGradient>
      <linearGradient id="g-gold" x1="0" y1="0" x2="1" y2="0"><stop offset="0" stop-color="#f0b560"/><stop offset="1" stop-color="#f5c57f"/></linearGradient>
      <linearGradient id="g-pink" x1="0" y1="0" x2="1" y2="0"><stop offset="0" stop-color="#e4507d"/><stop offset="1" stop-color="#e56a8d"/></linearGradient>
      <linearGradient id="g-orange" x1="0" y1="0" x2="1" y2="0.4"><stop offset="0" stop-color="#f3891f"/><stop offset="1" stop-color="#fb9160"/></linearGradient>
    </defs>
  </svg>

  <div class="sidebar">
    <svg viewBox="0 0 46 412" preserveAspectRatio="none" style="position:absolute;inset:0;width:46px;height:412px"><path d="M0 0Q44 18 46 40V178Q44 196 0 206Q44 218 46 236V376Q44 396 0 412Z" fill="#fff"/></svg>
    <span class="side-label__rule" style="left:9px;top:86px;height:30px;background:#2ec5e6"></span>
    <span class="side-label title-me" style="left:17px;top:136px">Why Me?</span>
    <span class="side-label__rule" style="left:9px;top:292px;height:30px;background:#f58a63"></span>
    <span class="side-label title-company" style="left:17px;top:375px">Why Brightfield?</span>
  </div>
  <div class="divider"></div>
  <div class="dots dots--cool" style="left:708px;top:16px"><i></i><i></i><i></i></div>
  <div class="dots dots--warm" style="left:708px;top:398px"><i></i><i></i><i></i></div>

  <!-- Superhero -->
  <div class="blob" style="left:66px;top:56px;width:196px;height:126px"><svg viewBox="0 0 100 60" preserveAspectRatio="none"><path d="M10 0H80Q101 0 99 18Q97 34 58 51Q16 66 5 44Q1 28 2 11Q3 0 10 0Z" fill="url(#g-blue)"/></svg></div>
  <div class="pill pill--blue" style="left:67px;top:43px;width:141px">If I was a superhero</div>
  <ul class="points blob-text" style="left:87px;top:77px">
    <li style="padding-left:0"><strong>My four superpowers would be:</strong></li>
    <li>Proactiveness</li><li>Creativity</li><li>Pride in my work</li><li>Organisational skills</li>
  </ul>
  <div class="placeholder" role="img" aria-label="Flying superhero illustration" style="left:198px;top:99px;width:34px;height:30px;background:rgba(255,255,255,.85)"></div>

  <!-- Success -->
  <div class="blob" style="left:272px;top:42px;width:224px;height:152px"><svg viewBox="0 0 100 60" preserveAspectRatio="none"><path d="M6 0H70Q100 4 99 24Q98 38 52 54Q14 66 6 46Q0 30 1 10Q2 0 6 0Z" fill="url(#g-purple)"/></svg></div>
  <div class="pill pill--purple" style="left:273px;top:33px;width:141px">Some of my success</div>
  <ul class="points blob-text" style="left:281px;top:67px;width:180px">
    <li>Increased client workshops by 85% across accounts.</li>
    <li>Delivered double digit revenue increase.</li>
    <li>Re-designed workshops for virtual delivery, maintaining key relationships.</li>
  </ul>
  <svg style="position:absolute;left:309px;top:157px;width:26px;height:22px" viewBox="0 0 16 14" fill="none" stroke="#fff" stroke-width="1.1"><rect x="1" y="1" width="11" height="8"/><path d="M3 6l2-2 2 2 3-3"/><circle cx="12.5" cy="8" r="1.6" fill="#fff"/><path d="M10 14v-2a2.5 2.5 0 015 0v2" fill="#fff"/></svg>

  <!-- Passion -->
  <div class="blob" style="left:507px;top:58px;width:218px;height:130px"><svg viewBox="0 0 100 60" preserveAspectRatio="none"><path d="M12 0H80Q101 2 99 20Q97 34 54 52Q16 66 6 45Q0 30 2 15Q4 0 12 0Z" fill="url(#g-teal)"/></svg></div>
  <div class="pill pill--teal" style="left:543px;top:40px;width:141px">Passion</div>
  <ul class="points blob-text" style="left:524px;top:73px;width:182px">
    <li>The development of others and / or their teams.</li>
    <li>Helping people learn and be successful in life and in their careers.</li>
    <li>Exceptional client</li><li>experiences</li>
  </ul>
  <svg style="position:absolute;left:646px;top:126px;width:30px;height:30px" viewBox="0 0 16 16" fill="#fff"><rect x="2" y="2" width="5.5" height="5.5" rx="1"/><rect x="8.5" y="2" width="5.5" height="5.5" rx="1"/><rect x="2" y="8.5" width="5.5" height="5.5" rx="1"/><rect x="8.5" y="8.5" width="5.5" height="5.5" rx="1"/></svg>

  <!-- Values -->
  <div class="blob" style="left:72px;top:258px;width:178px;height:126px"><svg viewBox="0 0 100 60" preserveAspectRatio="none"><path d="M8 0H80Q101 2 98 20Q95 34 50 53Q14 66 6 44Q0 28 2 12Q3 0 8 0Z" fill="url(#g-gold)"/></svg></div>
  <div class="pill pill--gold" style="left:76px;top:247px;width:151px">Values that stood out</div>
  <ul class="points blob-text" style="left:88px;top:281px">
    <li>Proactiveness</li><li>Creativity</li><li>Pride in my work</li><li>Organisational skills</li>
  </ul>
  <svg style="position:absolute;left:196px;top:288px;width:28px;height:28px" viewBox="0 0 32 32" fill="none" stroke="#fff" stroke-width="2.2"><circle cx="16" cy="16" r="14"/><path d="M16 2v14l10 8M16 16L5 24"/></svg>

  <!-- Offer -->
  <div class="blob" style="left:279px;top:256px;width:180px;height:108px"><svg viewBox="0 0 100 60" preserveAspectRatio="none"><path d="M14 0H78Q101 4 98 28Q95 42 60 54Q20 66 6 50Q0 38 2 22Q5 2 14 0Z" fill="url(#g-pink)"/></svg></div>
  <div class="pill pill--pink" style="left:295px;top:247px;width:141px">What you offer</div>
  <ul class="points blob-text" style="left:297px;top:286px">
    <li>Learning &amp; Developing</li><li>Team</li><li>Flexibility</li><li>Fun</li>
  </ul>
  <svg style="position:absolute;left:403px;top:304px;width:26px;height:26px" viewBox="0 0 16 16" fill="#fff"><rect x="1" y="9" width="2.5" height="6"/><rect x="4.8" y="7" width="2.5" height="8"/><rect x="8.6" y="8" width="2.5" height="7"/><rect x="12.4" y="10" width="2.5" height="5"/><circle cx="8" cy="3" r="2"/></svg>

  <!-- Projects -->
  <div class="blob" style="left:487px;top:233px;width:238px;height:158px"><svg viewBox="0 0 100 60" preserveAspectRatio="none"><path d="M14 0H75Q101 4 99 24Q97 37 58 53Q18 66 7 48Q0 34 1 18Q3 0 14 0Z" fill="url(#g-orange)"/></svg></div>
  <div class="pill pill--orange" style="left:559px;top:238px;width:142px">Interesting projects</div>
  <svg style="position:absolute;left:517px;top:248px;width:22px;height:22px" viewBox="0 0 16 16" fill="none" stroke="#fff" stroke-width="1.2"><rect x="1" y="1.5" width="14" height="10"/><path d="M3.5 9l3-3 2 2 4-4M8 11.5V14M5 15l3-1.5 3 1.5"/></svg>
  <ul class="points blob-text" style="left:499px;top:273px;width:192px">
    <li>Ovela - Leadership development and team effectiveness</li>
    <li>Hartwell – Change management for true transformation</li>
    <li>Lyra – Customer centricity at Australia's most iconic department store</li>
  </ul>
</section>

</body>
</html>
```